Plakate für eine KFZ Werkstatt
Zielgruppe
KFZ Werkstatt, KFZ Lackiererei, Fahrzeugaufbereitung
Meine Zielgruppe ist Regional.
Aufgabenstellung
Es sind zwei Firmen die beide mir sind. Beide Logos und der Slogan sollen zu sehen sein.
Das Banner soll 12 Meter lang und 2 Meter hoch sein. Das Banner ist dunkelgrün. Die Schrift soll weiß sein. (Banner kommt auf einen Tennisplatz)

```html
<!DOCTYPE html>
<html lang="de">
<head>
<meta charset="utf-8">
<title>Bannerwerbung Tennisplatz – Glanzwerk Studio & Auto Ferbolz</title>
<link href="https://fonts.googleapis.com/css2?family=Oswald:wght@500;600&family=Roboto+Condensed:wght@400&family=Saira:wght@400&display=swap" rel="stylesheet">
<style>
  :root {
    --page-bg: #ececec;
    --banner-green: #006330;
    --banner-green-deep: #005128;
    --splash-green: #00401f;
    --text-white: #ffffff;
    --tab-text-green: #00602e;
  }
  * { margin: 0; padding: 0; box-sizing: border-box; }
  html, body {
    width: 1200px;
    height: 790px;
    overflow: hidden;
    background: var(--page-bg);
  }
  .canvas {
    position: relative;
    width: 1200px;
    height: 790px;
  }
  .banner {
    position: absolute;
    left: 30px;
    top: 300px;
    width: 1140px;
    height: 190px;
    background: var(--banner-green);
    overflow: hidden;
    color: var(--text-white);
  }
  .banner__right-field {
    position: absolute;
    left: 700px;
    top: 0;
    right: 0;
    bottom: 0;
    background: var(--banner-green-deep);
  }
  .banner__splash {
    position: absolute;
    left: 660px;
    top: 40px;
    width: 90px;
    height: 150px;
    background: linear-gradient(90deg, rgba(0,64,31,0) 0%, var(--splash-green) 55%, var(--banner-green-deep) 100%);
  }
  .slogan-tab {
    position: absolute;
    left: 572px;
    top: 0;
    width: 226px;
    height: 40px;
    background: var(--text-white);
    border-radius: 0 0 14px 14px;
    display: flex;
    align-items: center;
    justify-content: center;
  }
  .slogan-tab__text {
    font-family: "Oswald", sans-serif;
    font-weight: 600;
    font-size: 25px;
    color: var(--tab-text-green);
    letter-spacing: -0.3px;
  }
  .brand-left {
    position: absolute;
    left: 40px;
    top: 48px;
    width: 620px;
    text-align: center;
  }
  .brand-left__name {
    font-family: "Oswald", sans-serif;
    font-weight: 600;
    font-size: 50px;
    line-height: 1;
    color: var(--text-white);
  }
  .brand-left__tagline {
    margin-top: 16px;
    font-family: "Saira", sans-serif;
    font-weight: 400;
    font-size: 19px;
    color: var(--text-white);
  }
  .brand-right {
    position: absolute;
    left: 790px;
    top: 48px;
    display: flex;
    align-items: center;
    gap: 16px;
  }
  .brand-right__mark {
    width: 96px;
    height: 96px;
    flex: none;
  }
  .brand-right__text {
    font-family: "Roboto Condensed", sans-serif;
    font-weight: 400;
    color: var(--text-white);
  }
  .brand-right__kicker {
    font-size: 19px;
    line-height: 1.1;
  }
  .brand-right__name {
    font-size: 44px;
    line-height: 1.05;
  }
  .brand-right__services {
    margin-top: 4px;
    font-size: 15px;
    line-height: 1.1;
    white-space: nowrap;
  }
  .brand-right__divider {
    display: inline-block;
    margin: 0 8px;
  }
</style>
</head>
<body>
  <div class="canvas">
    <section class="banner" aria-label="Werbebanner 12 × 2 Meter">
      <div class="banner__right-field"></div>
      <div class="banner__splash" role="img" aria-label="Dunkelgrüner Farbspritzer als Übergang zwischen beiden Firmen"></div>

      <div class="slogan-tab">
        <span class="slogan-tab__text">Das perfekte Doppel</span>
      </div>

      <div class="brand-left">
        <div class="brand-left__name">Glanzwerk Studio</div>
        <div class="brand-left__tagline">Ihr Partner für professionelle KFZ-Aufbereitung</div>
      </div>

      <div class="brand-right">
        <svg class="brand-right__mark" viewBox="0 0 96 96" aria-hidden="true">
          <circle cx="48" cy="48" r="45" fill="none" stroke="#ffffff" stroke-width="4"/>
        </svg>
        <div class="brand-right__text">
          <div class="brand-right__kicker">Der neue</div>
          <div class="brand-right__name">Auto Ferbolz</div>
          <div class="brand-right__services">Karosserie<span class="brand-right__divider">|</span>Lackiererei<span class="brand-right__divider">|</span>Mechanik</div>
        </div>
      </div>
    </section>
  </div>
</body>
</html>
```